Financial Services Business Card Design

We are a financial services company Based in London, offering Short term Funding Solutions for companies, raising anywhere between £20,000 and £25million pounds.

The Card must have a professional look as it is going to be handed out to professionals I.E Solicitors, Accountants, Company directors and Business owners.

See Attached our company Logo

Industry/Entity Type

Business

Contact Information for Business Card

Brett Kolvane
Suite 41
R T House
Hazelbrook Lane
Watford
WD17 4QL

```html
<!DOCTYPE html>
<html lang="en">
<head>
<meta charset="UTF-8">
<title>Meridian Bridge Finance – Business Card</title>
<link href="https://fonts.googleapis.com/css2?family=Open+Sans:wght@400;600;700&display=swap" rel="stylesheet">
<style>
  :root {
    --backdrop: #3b3b3d;
    --card: #050505;
    --blue: #1b7bc4;
    --green: #35b44a;
    --white: #f2f2f2;
    --rule: #6a6a6a;
  }
  * { margin: 0; padding: 0; box-sizing: border-box; }
  html, body {
    width: 1200px; height: 900px; overflow: hidden;
    background: var(--backdrop);
    font-family: "Open Sans", Arial, sans-serif;
  }
  .canvas {
    position: relative; width: 1200px; height: 900px;
  }
  .card {
    position: absolute; left: 290px;
    width: 620px; height: 354px;
    background: var(--card);
    border-radius: 26px;
    box-shadow: 0 14px 30px rgba(0,0,0,0.45);
  }
  .card--front { top: 66px; }
  .card--back { top: 480px; }

  .front-brand {
    position: absolute; inset: 0;
    display: flex; align-items: center; justify-content: center; gap: 16px;
  }
  .brand-dot {
    width: 30px; height: 30px; border-radius: 50%;
    background: var(--green);
  }
  .brand-name {
    color: var(--blue); font-weight: 700; letter-spacing: 1px;
    text-transform: uppercase;
  }
  .front-brand .brand-name { font-size: 34px; }

  .back-brand {
    position: absolute; left: 40px; top: 0; bottom: 0; width: 250px;
    display: flex; flex-direction: column; justify-content: center; gap: 10px;
  }
  .back-brand .brand-dot { width: 22px; height: 22px; }
  .back-brand .brand-name { font-size: 25px; line-height: 1.15; }

  .divider {
    position: absolute; left: 312px; top: 92px;
    width: 1px; height: 170px; background: var(--rule);
  }
  .contact {
    position: absolute; left: 336px; top: 104px; right: 24px;
    color: var(--white);
  }
  .contact-name {
    font-size: 22px; font-weight: 600; letter-spacing: 1.5px;
    text-transform: uppercase; margin-bottom: 12px;
  }
  .contact-name .first { color: var(--blue); }
  .contact-name .last { color: var(--green); }
  .address { font-size: 14px; line-height: 1.45; margin-bottom: 14px; }
  .line { display: flex; align-items: center; gap: 8px; font-size: 14px; line-height: 1.6; }
  .line svg { width: 12px; height: 12px; flex: none; }
</style>
</head>
<body>
<main class="canvas">
  <section class="card card--front">
    <div class="front-brand">
      <span class="brand-dot"></span>
      <span class="brand-name">Meridian Bridge Finance</span>
    </div>
  </section>

  <section class="card card--back">
    <div class="back-brand">
      <span class="brand-dot"></span>
      <span class="brand-name">Meridian Bridge Finance</span>
    </div>
    <div class="divider"></div>
    <div class="contact">
      <p class="contact-name"><span class="first">Brett</span> <span class="last">Kolvane</span></p>
      <p class="address">Suite 41, R T House,<br>Hazelbrook Lane, Watford, WD17 4QL</p>
      <p class="line">
        <svg viewBox="0 0 24 24" aria-hidden="true"><path fill="#35b44a" d="M6.6 10.8a15.1 15.1 0 0 0 6.6 6.6l2.2-2.2c.3-.3.7-.4 1-.2 1.1.4 2.3.6 3.6.6.6 0 1 .4 1 1V20c0 .6-.4 1-1 1A17 17 0 0 1 3 4c0-.6.4-1 1-1h3.5c.6 0 1 .4 1 1 0 1.3.2 2.5.6 3.6.1.3 0 .7-.2 1z"/></svg>
        +44 1923 555 0147
      </p>
      <p class="line">
        <svg viewBox="0 0 24 24" aria-hidden="true"><rect x="2" y="5" width="20" height="14" rx="2" fill="none" stroke="#35b44a" stroke-width="2.5"/><path d="M3 6l9 7 9-7" fill="none" stroke="#35b44a" stroke-width="2.5"/></svg>
        info@brettkolvane.co.uk
      </p>
    </div>
  </section>
</main>
</body>
</html>
```